Stationery design for a hip Muslim Travel Agency

We are looking for a colorful and energetic stationery design for a Muslim tour and travel agency. We need a letterhead, A4 folder, business card and loyalty card design.

The designs should be clean and cheerful and have a feeling of a colorful mosaic in a mosque. You can use the Mingleroo avatar and cover photo as the basis.

Pelitaru card is a loyalty card we issue to our clients. This can have a similar feel to the business card and it should NOT have the word "card" added to the logo. Think of airline membership cards.

Target Market(s)

Indonesians, 25-44 years old, Muslim, interesting in Umroh and Haji and other Muslim tours.

Industry/Entity Type

Travel Agent

Contact Information for Business Card

As provided in the .psd file.

Font styles to use
Sans Serif

Colors
27a0d5
33b8a4
00a990
0492cd

Requirements
Must have
• Letterhead design
• A4 folder design
• Business card
• Loyalty card (without the word "card" in the logo)
Nice to have
• Use the mosaic patterns provided in the files. We want to express the theme of colorful Islam.
Should not have
• Don't copy the .psd files provided in the brief. This is just for the content, those files were not prepared by a designer.

```html
<!DOCTYPE html>
<html lang="en">
<head>
<meta charset="utf-8">
<title>Pelitaru Stationery</title>
<link href="https://fonts.googleapis.com/css2?family=Oxanium:wght@700&family=Lato:wght@400;700&family=Share+Tech+Mono&family=Homemade+Apple&display=swap" rel="stylesheet">
<style>
:root{
  --bg:#d1d2d4;
  --teal:#10b5a3;
  --green:#a6ce39;
  --ink:#1d1d1b;
  --grey:#8a8a8a;
  --white:#ffffff;
  --pattern:linear-gradient(180deg,#7cc34c 0%,#3dbb82 55%,#10b5a3 100%);
  --strip:linear-gradient(180deg,#10b5a3 0%,#4dbd78 50%,#a6ce39 100%);
}
*{margin:0;padding:0;box-sizing:border-box}
html,body{width:1200px;height:1200px;overflow:hidden;background:var(--bg)}
.canvas{position:relative;width:1200px;height:1200px;font-family:'Lato',sans-serif;color:var(--ink)}
.brand{font-family:'Oxanium',sans-serif;font-weight:700;letter-spacing:.5px}
.shadow{box-shadow:0 6px 10px rgba(0,0,0,.18)}
.abs{position:absolute}

/* folder */
.folder-flaps{position:absolute;left:0;top:0}
.folder{left:235px;top:94px;width:625px;height:441px;background:var(--teal)}
.folder-pattern{left:0;top:0;width:313px;height:441px;background:var(--pattern)}
.folder-brand{left:313px;width:312px;top:230px;text-align:center;color:var(--white);font-size:31px}
.folder-contacts{left:0;top:386px;width:313px;display:flex;justify-content:space-around;color:var(--white);font-size:4.5px;text-align:center}
.folder-contacts svg{display:block;margin:0 auto 3px}

/* loyalty card */
.card{background:var(--white);border-radius:8px;overflow:hidden}
.loyalty-front{left:180px;top:704px;width:217px;height:136px}
.loyalty-strip{right:0;top:0;width:63px;height:136px;background:var(--strip)}
.logo-row{display:flex;align-items:center;gap:4px}
.logo-dot{width:16px;height:16px;border-radius:50%;background:var(--teal)}
.loyalty-front .logo-row{left:17px;top:16px;font-size:14px}
.loyalty-title{left:18px;top:60px;font-size:12px}
.loyalty-number{left:18px;top:78px;font-family:'Share Tech Mono',monospace;font-size:9px}
.loyalty-valid{left:82px;top:89px;font-size:5px}
.loyalty-holder{left:18px;top:113px;font-size:7.5px}

.loyalty-back{left:288px;top:831px;width:216px;height:136px;text-align:center}
.mag-stripe{left:0;top:16px;width:216px;height:24px;background:var(--ink)}
.back-lead{left:0;top:47px;width:216px;font-size:4.8px}
.back-title{left:0;top:58px;width:216px;font-size:11px}
.back-body{left:20px;top:82px;width:176px;font-size:4.8px;line-height:1.35}
.back-contact{font-size:4px;display:flex;align-items:center;gap:3px}

/* letterhead */
.letterhead{left:566px;top:619px;width:319px;height:451px;background:var(--white)}
.letter-strip{left:0;top:0;width:44px;height:451px;background:var(--strip)}
.letterhead .logo-row{left:64px;top:42px;font-size:14px}
.letter-greeting{left:64px;top:103px;font-size:5px}
.letter-body{left:64px;top:138px;width:234px;font-size:4.6px;line-height:1.38;color:var(--grey)}
.letter-body p{margin-bottom:5px}
.letter-sign{left:64px;top:296px;width:48px;border-bottom:.6px solid var(--ink);font-family:'Homemade Apple',cursive;font-size:6px;color:var(--grey)}
.letter-contacts{left:64px;top:378px;font-size:3.6px;line-height:2}
.letter-contacts .back-contact{font-size:3.6px}

/* business card */
.biz-front{left:873px;top:695px;width:201px;height:116px;background:var(--teal);text-align:center}
.biz-front .brand{position:absolute;left:0;width:201px;top:56px;color:var(--white);font-size:17px}
.biz-back{left:873px;top:837px;width:201px;height:115px;background:var(--white)}
.biz-strip{right:0;top:0;width:54px;height:115px;background:var(--strip)}
.biz-back .logo-row{left:18px;top:20px;font-size:11.5px}
.biz-name{left:18px;top:47px;font-size:6px}
.biz-role{left:18px;top:55px;font-size:4.2px;color:var(--teal)}
.biz-contacts{left:18px;top:68px;line-height:1.9}
.biz-contacts .back-contact{font-size:3.6px}
</style>
</head>
<body>
<div class="canvas">

  <svg class="folder-flaps" width="1200" height="1200" aria-hidden="true">
    <polygon points="174,132 235,94 235,535 174,488" fill="#a6ce39"/>
    <polygon points="235,535 548,535 496,610 235,610" fill="#a6ce39"/>
  </svg>

  <section class="abs folder shadow">
    <div class="abs folder-pattern" role="img" aria-label="Mosque mosaic star pattern in green and teal"></div>
    <div class="abs folder-contacts">
      <div><svg width="8" height="8" viewBox="0 0 10 10"><path d="M2 1l2 2-1 1.5a5 5 0 002.5 2.5L7 6l2 2-1.5 1.5C4 9 1 6 .5 2.5z" fill="#fff"/></svg>+0210 44817</div>
      <div><svg width="8" height="8" viewBox="0 0 10 10"><rect x="1" y="2.5" width="8" height="5.5" fill="#fff"/><path d="M1 2.5l4 3 4-3" stroke="#10b5a3" stroke-width=".8" fill="none"/></svg>info@pelitaru.id</div>
      <div><svg width="8" height="8" viewBox="0 0 10 10"><path d="M5 .5a3.3 3.3 0 00-3.3 3.3C1.7 6.5 5 9.5 5 9.5s3.3-3 3.3-5.7A3.3 3.3 0 005 .5z" fill="#fff"/><circle cx="5" cy="3.8" r="1.2" fill="#10b5a3"/></svg>418 Larch Row, Fenmore, MA 01077</div>
    </div>
    <div class="abs folder-brand brand">pelitaru.id</div>
  </section>

  <section class="abs card loyalty-front shadow">
    <div class="abs loyalty-strip" role="img" aria-label="Mosaic star pattern strip"></div>
    <div class="abs logo-row brand"><span class="logo-dot"></span>pelitaru.id</div>
    <div class="abs loyalty-title brand">Loyalty</div>
    <div class="abs loyalty-number">0123 4567 8901 2345</div>
    <div class="abs loyalty-valid">Valid :07/18</div>
    <div class="abs loyalty-holder brand">Lorem Ipsum</div>
  </section>

  <section class="abs card loyalty-back shadow">
    <div class="abs mag-stripe"></div>
    <p class="abs back-lead">Lorem Ipsum is simply dummy text of the printing and typesetting industry.</p>
    <h2 class="abs back-title brand">Lorem Ipsum</h2>
    <p class="abs back-body">Lorem Ipsum is simply dummy text of the printing and typesetting industry. Lorem Ipsum has been the industry's standard dummy text ever since the 1500s, when an unknown printer took a galley of type and scrambled it to make a type specimen book.</p>
    <div class="abs back-contact" style="left:24px;top:119px"><svg width="5" height="5" viewBox="0 0 10 10"><path d="M2 1l2 2-1 1.5a5 5 0 002.5 2.5L7 6l2 2-1.5 1.5C4 9 1 6 .5 2.5z" fill="#10b5a3"/></svg>+0210 44818</div>
    <div class="abs back-contact" style="left:146px;top:119px"><svg width="5" height="5" viewBox="0 0 10 10"><rect x="1" y="2.5" width="8" height="5.5" fill="#10b5a3"/></svg>info@pelitaru.id</div>
    <div class="abs back-contact" style="left:63px;top:127px"><svg width="5" height="5" viewBox="0 0 10 10"><path d="M5 .5a3.3 3.3 0 00-3.3 3.3C1.7 6.5 5 9.5 5 9.5s3.3-3 3.3-5.7A3.3 3.3 0 005 .5z" fill="#10b5a3"/></svg>418 Larch Row, Fenmore, MA 01077</div>
  </section>

  <section class="abs letterhead shadow">
    <div class="abs letter-strip" role="img" aria-label="Mosaic star pattern border"></div>
    <div class="abs logo-row brand"><span class="logo-dot"></span>pelitaru.id</div>
    <p class="abs letter-greeting">Dear, Mr_________</p>
    <div class="abs letter-body">
      <p>Lorem Ipsum is simply dummy text of the printing and typesetting industry. Lorem Ipsum has been the industry's standard dummy text ever since the 1500s, when an unknown printer took a galley of type and scrambled it to make a type specimen book. It has survived not only five centuries, but also the leap into electronic typesetting, remaining essentially unchanged. It was popularised in the 1960s with the release of Letraset sheets containing Lorem Ipsum passages, and more recently with desktop publishing software like Aldus PageMaker including versions of Lorem Ipsum.</p>
      <p>Lorem Ipsum is simply dummy text of the printing and typesetting industry. Lorem Ipsum has been the industry's standard dummy text ever since the 1500s, when an unknown printer took a galley of type and scrambled it to make a type specimen book.</p>
      <p>Lorem Ipsum is simply dummy text of the printing and typesetting industry. Lorem Ipsum has been the industry's standard dummy text ever since the 1500s, when an unknown printer took a galley of type and scrambled it to make a type specimen book. It has survived not only five centuries, but also the leap into electronic typesetting, remaining essentially unchanged.</p>
      <p>Lorem Ipsum is simply dummy text of the printing and typesetting industry. Lorem Ipsum has been the industry's standard dummy text ever since the 1500s.</p>
    </div>
    <div class="abs letter-sign">Signature</div>
    <div class="abs letter-contacts">
      <div class="back-contact"><svg width="4" height="4" viewBox="0 0 10 10"><circle cx="5" cy="5" r="4" fill="#10b5a3"/></svg>+0210 44817</div>
      <div class="back-contact"><svg width="4" height="4" viewBox="0 0 10 10"><rect x="1" y="2.5" width="8" height="5.5" fill="#10b5a3"/></svg>info@pelitaru.id</div>
      <div class="back-contact"><svg width="4" height="4" viewBox="0 0 10 10"><circle cx="5" cy="5" r="4" fill="none" stroke="#10b5a3" stroke-width="1.5"/></svg>www.pelitaru.id</div>
      <div class="back-contact"><svg width="4" height="4" viewBox="0 0 10 10"><path d="M5 .5a3.3 3.3 0 00-3.3 3.3C1.7 6.5 5 9.5 5 9.5s3.3-3 3.3-5.7A3.3 3.3 0 005 .5z" fill="#10b5a3"/></svg>418 Larch Row, Fenmore, MA 01077</div>
    </div>
  </section>

  <section class="abs biz-front shadow">
    <div class="brand">pelitaru.id</div>
  </section>

  <section class="abs biz-back shadow">
    <div class="abs biz-strip" role="img" aria-label="Mosaic star pattern strip"></div>
    <div class="abs logo-row brand"><span class="logo-dot" style="width:13px;height:13px"></span>pelitaru.id</div>
    <div class="abs biz-name brand">Dara Quillfen</div>
    <div class="abs biz-role brand">Director</div>
    <div class="abs biz-contacts">
      <div class="back-contact"><svg width="4" height="4" viewBox="0 0 10 10"><circle cx="5" cy="5" r="4" fill="#10b5a3"/></svg>+0210 44818</div>
      <div class="back-contact"><svg width="4" height="4" viewBox="0 0 10 10"><rect x="1" y="2.5" width="8" height="5.5" fill="#10b5a3"/></svg>info@pelitaru.id</div>
      <div class="back-contact"><svg width="4" height="4" viewBox="0 0 10 10"><circle cx="5" cy="5" r="4" fill="none" stroke="#10b5a3" stroke-width="1.5"/></svg>www.pelitaru.id</div>
      <div class="back-contact" style="margin-top:3px"><svg width="4" height="4" viewBox="0 0 10 10"><path d="M5 .5a3.3 3.3 0 00-3.3 3.3C1.7 6.5 5 9.5 5 9.5s3.3-3 3.3-5.7A3.3 3.3 0 005 .5z" fill="#10b5a3"/></svg>418 Larch Row, Fenmore, MA 01077</div>
    </div>
  </section>

</div>
</body>
</html>
```